Flyer for Library Conference on Information Literacy

We need a flyer for a library conference called QUIVA. It will be held in Naperville, IL and the theme we are going for is trees/spring because there is an arboretum nearby and the conference is in May. We will need the following large text:
QUIVA 2024
Naperville, IL
May 2-4

And then we'll need the "name" of the 2024 conference, which is as follows:
Open Horizons: Shaping and Renewing your Research Teaching Craft
And then these 6 track names:
Planting Seeds: Pedagogy & Instructional Design
Putting Down Roots: Collaboration & Outreach
Seeing the Forest: Assessment & Evaluation
Controlled Burns: Revitalize & Renew
Climate Change: Adapting to New Technologies
Field Notes: Using Research to Inform Practice
Here is a color palette we were thinking about: https://huebinder.example/dune-meadow-ridge-shade-set/
But we are open to other ideas. We are thinking of trees
We'd like images of trees (though not photographs and not pine trees.) Here are a few examples (though these are photographs):
https://velmagrove.example/grow-and-guard/find-shrubs-and-flora/?query_text=&fl_kind_type=shrub
https://flora.outreach.tamblin.example/notes/western-goldleaf-acer-brevis/
Something on the minimalistic side, calming, nature

Target Market(s)

Librarians

Font styles to use
Sans Serif

Colors

Designer to choose colors to be used in the design.

Requirements
Must have
• The following text: QUIVA 2024, Naperville, IL , Open Horizons: Shaping and Renewing your Research Teaching Craft, Planting Seeds: Pedagogy & Instructional Design Putting Down Roots: Collaboration & Outreach Seeing the Forest: Assessment & Evaluation Controlled Burns: Revitalize & Renew Climate Change: Adapting to New Technologies Field Notes: Using Research to Inform Practice
Should not have
• photographs

```html
<!DOCTYPE html>
<html lang="en">
<head>
<meta charset="utf-8">
<title>QUIVA 2024 Conference Flyer</title>
<link href="https://fonts.googleapis.com/css2?family=Montserrat:wght@600;700;800&family=Roboto+Condensed:wght@700&family=Roboto:wght@500&display=swap" rel="stylesheet">
<style>
  :root {
    --page-bg: #e4e4e4;
    --paper: #ffffff;
    --cream: #f7f5d6;
    --leaf: #78b03c;
    --leaf-mid: #8cbf4f;
    --forest: #4f7d2e;
    --forest-deep: #3f6a24;
    --theme-green: #4e8a2c;
    --title-blue: #2e4fa0;
    --date-blue: #7591cc;
    --pin-red: #c8272d;
    --ink: #222222;
  }
  * { box-sizing: border-box; margin: 0; padding: 0; }
  html, body { width: 1046px; height: 1200px; overflow: hidden; background: var(--page-bg); }
  .flyer {
    position: absolute; left: 99px; top: 0; width: 848px; height: 1200px;
    background: var(--paper); overflow: hidden;
  }
  .flyer-art { position: absolute; inset: 0; }
  .scene-art {
    position: absolute; left: 0; top: 0; width: 848px; height: 1200px;
    clip-path: path('M478 0 C448 70 424 140 440 192 C458 285 505 380 546 434 C600 502 705 527 848 534 V0 Z');
    background: linear-gradient(160deg, #f1f6ea 0%, #a9d47a 55%, #6fa63b 100%);
  }
  .tree-backdrop {
    position: absolute; left: 640px; top: 580px; width: 208px; height: 360px;
    border-radius: 50% 0 0 40%;
    background: radial-gradient(ellipse at 70% 40%, rgba(200,222,160,0.45) 0%, rgba(247,245,214,0) 70%);
  }
  .grass-band {
    position: absolute; left: 0; top: 930px; width: 848px; height: 110px;
    background: linear-gradient(180deg, rgba(140,191,79,0) 0%, #7cbc44 70%, #5e9a32 100%);
  }
  .brand {
    position: absolute; left: 138px; top: 158px; width: 200px;
    display: flex; align-items: center; justify-content: center; gap: 10px;
    font-family: "Montserrat", sans-serif; font-weight: 800; font-size: 34px;
    color: var(--title-blue); letter-spacing: 1px;
  }
  .brand-dot { width: 22px; height: 22px; border-radius: 50%; background: var(--leaf); }
  .event-title {
    position: absolute; left: 0; width: 476px; top: 296px; text-align: center;
    font-family: "Roboto Condensed", sans-serif; font-weight: 700; font-size: 90px;
    line-height: 1; color: var(--title-blue);
  }
  .event-theme {
    position: absolute; left: 0; width: 476px; top: 398px; text-align: center;
    font-family: "Roboto", sans-serif; font-weight: 500; font-size: 32px;
    line-height: 40px; color: var(--theme-green);
  }
  .date-pill {
    position: absolute; left: 0; top: 584px; width: 442px; height: 68px;
    background: var(--date-blue); border-radius: 0 34px 34px 0;
    display: flex; align-items: center; padding-left: 74px; gap: 14px;
    font-family: "Montserrat", sans-serif; font-weight: 700; font-size: 36px; color: #fff;
  }
  .tracks {
    position: absolute; left: 28px; top: 690px; width: 800px;
    display: grid; grid-template-columns: 401px 399px; row-gap: 15px;
    list-style: none;
  }
  .track { display: flex; align-items: center; gap: 22px; height: 61px; }
  .track-icon {
    flex: none; width: 61px; height: 61px; border-radius: 50%;
    background: var(--theme-green); border: 3px solid #fff;
    box-shadow: 0 0 0 1px #d8e8c4;
    display: flex; align-items: center; justify-content: center;
  }
  .track-name {
    font-family: "Montserrat", sans-serif; font-weight: 800; font-size: 18px;
    color: var(--theme-green); line-height: 24px;
  }
  .track-focus {
    font-family: "Montserrat", sans-serif; font-weight: 600; font-size: 16px;
    color: var(--ink); line-height: 22px;
  }
  .venue {
    position: absolute; left: 436px; top: 1108px;
    font-family: "Montserrat", sans-serif; font-weight: 700; font-size: 40px;
    color: #fff; line-height: 50px;
  }
</style>
</head>
<body>
<main class="flyer">
  <svg class="flyer-art" width="848" height="1200" viewBox="0 0 848 1200" aria-hidden="true">
    <defs>
      <linearGradient id="corner-wash" x1="0" y1="0" x2="1" y2="1">
        <stop offset="0" stop-color="#b9e08f"/>
        <stop offset="1" stop-color="#ffffff" stop-opacity="0"/>
      </linearGradient>
    </defs>
    <path d="M0 0 H420 C380 120 260 260 0 270 Z" fill="url(#corner-wash)"/>
    <path d="M0 560 C40 530 70 520 110 545 C160 510 230 520 270 548 C330 525 380 520 420 540 C520 560 620 520 848 560 V1200 H0 Z" fill="var(--cream)"/>
    <path d="M0 1000 C120 980 200 1060 320 1020 C460 970 600 1010 848 960 V1200 H0 Z" fill="var(--leaf-mid)"/>
    <path d="M0 1050 C140 1080 260 1010 400 1030 C560 1060 700 1000 848 1020 V1200 H0 Z" fill="var(--forest)"/>
    <path d="M0 1120 C200 1140 420 1090 848 1130 V1200 H0 Z" fill="var(--forest-deep)"/>
    <path d="M382 1100 H760 L822 1164 H382 Z" fill="var(--leaf-mid)"/>
    <path d="M382 1070 C360 1070 346 1086 346 1106 C346 1132 382 1164 382 1164 C382 1164 418 1132 418 1106 C418 1086 404 1070 382 1070 Z" fill="var(--pin-red)"/>
    <circle cx="382" cy="1104" r="12" fill="var(--forest)"/>
    <path d="M462 0 C430 70 405 140 421 192 C440 290 490 390 534 448 C590 520 700 545 848 552 V0 Z" fill="var(--leaf)"/>
  </svg>
  <div class="scene-art" role="img" aria-label="Illustration of people planting young leafy trees beside round green trees and hills"></div>
  <div class="tree-backdrop" role="img" aria-label="Faint illustrated tree with spreading branches and spring leaves"></div>
  <div class="grass-band" role="img" aria-label="Illustrated band of grass blades"></div>

  <div class="brand"><span class="brand-dot"></span>QUIVA</div>

  <h1 class="event-title">QUIVA 2024</h1>
  <p class="event-theme">Open Horizons:<br>Shaping and Renewing<br>your Research<br>Teaching Craft</p>

  <div class="date-pill">
    <svg width="44" height="44" viewBox="0 0 44 44" fill="none" stroke="#fff" stroke-width="2">
      <rect x="3" y="7" width="32" height="28" rx="2"/>
      <path d="M3 14 H35 M10 3 V10 M28 3 V10"/>
      <path d="M8 19 h4 M15 19 h4 M22 19 h4 M8 25 h4 M15 25 h4"/>
      <circle cx="33" cy="33" r="9" fill="var(--date-blue)"/>
      <path d="M29 33 l3 3 l5 -6"/>
    </svg>
    <span>May 2-4, 2023</span>
  </div>

  <ul class="tracks">
    <li class="track">
      <span class="track-icon"><svg width="30" height="30" viewBox="0 0 30 30" fill="none" stroke="#fff" stroke-width="2"><rect x="6" y="4" width="18" height="23" rx="2"/><path d="M11 10 h8 M11 15 h8 M11 20 h5"/></svg></span>
      <div><p class="track-name">Planting Seeds:</p><p class="track-focus">Pedagogy &amp; Instructional Design</p></div>
    </li>
    <li class="track">
      <span class="track-icon"><svg width="30" height="30" viewBox="0 0 30 30" fill="none" stroke="#fff" stroke-width="2"><path d="M24 9 a10 10 0 0 0 -17 -2 M6 21 a10 10 0 0 0 17 2"/><path d="M24 3 v6 h-6 M6 27 v-6 h6"/></svg></span>
      <div><p class="track-name">Controlled Burns:</p><p class="track-focus">Revitalize &amp; Renew</p></div>
    </li>
    <li class="track">
      <span class="track-icon"><svg width="30" height="30" viewBox="0 0 30 30" fill="none" stroke="#fff" stroke-width="2"><circle cx="10" cy="10" r="5"/><circle cx="20" cy="10" r="5"/><path d="M3 26 c1 -7 13 -7 14 0 M13 26 c1 -7 13 -7 14 0"/></svg></span>
      <div><p class="track-name">Putting Down Roots:</p><p class="track-focus">Collaboration &amp; Outreach</p></div>
    </li>
    <li class="track">
      <span class="track-icon"><svg width="30" height="30" viewBox="0 0 30 30" fill="none" stroke="#fff" stroke-width="2"><rect x="8" y="8" width="14" height="14" rx="2"/><path d="M12 3 v5 M18 3 v5 M12 22 v5 M18 22 v5 M3 12 h5 M3 18 h5 M22 12 h5 M22 18 h5"/></svg></span>
      <div><p class="track-name">Climate Change:</p><p class="track-focus">Adapting to New Technologies</p></div>
    </li>
    <li class="track">
      <span class="track-icon"><svg width="30" height="30" viewBox="0 0 30 30" fill="none" stroke="#fff" stroke-width="2"><rect x="5" y="3" width="18" height="24" rx="2"/><circle cx="14" cy="14" r="5"/><path d="M12 14 l2 2 l3 -4"/></svg></span>
      <div><p class="track-name">Seeing the Forest:</p><p class="track-focus">Assessment &amp; Evaluation</p></div>
    </li>
    <li class="track">
      <span class="track-icon"><svg width="30" height="30" viewBox="0 0 30 30" fill="none" stroke="#fff" stroke-width="2.4"><circle cx="12" cy="12" r="8"/><path d="M18 18 l9 9"/></svg></span>
      <div><p class="track-name">Field Notes:</p><p class="track-focus">Using Research to Inform Practice</p></div>
    </li>
  </ul>

  <p class="venue">Naperville, IL</p>
</main>
</body>
</html>
```